3" Round Business Card for Funeral Home

We need a business card designed for our cremation service. We would like to use a 3" round business card.

The business card will be 2-sided. One side with the logo featured prominently. The back sad will have employee name and contact info.

Templates for printing have been attached to project as well as logo

We like soft colors like the logo. Final design should promote a feeling of trust.

Industry/Entity Type

Funeral

Contact Information for Business Card

Employee Name, Phone number, email, web address

Requirements
Should not have
• any sort of funeral item such as urn, casket, hearse, tombstone

```html
<!DOCTYPE html>
<html lang="en">
<head>
<meta charset="utf-8">
<title>Serene Ember – Round Business Card</title>
<link rel="stylesheet" href="https://fonts.googleapis.com/css2?family=Jost:wght@400;500&family=Mr+Dafoe&display=swap">
<style>
  :root {
    --backdrop: #a4a4a4;
    --plum: #92278f;
    --teal: #1ba39b;
    --paper: #ffffff;
  }
  html, body {
    margin: 0;
    padding: 0;
    width: 1125px;
    height: 1200px;
    overflow: hidden;
    background: var(--backdrop);
  }
  .canvas {
    position: relative;
    width: 1125px;
    height: 1200px;
    font-family: "Jost", "Futura", sans-serif;
  }
  .card {
    position: absolute;
    top: 348px;
    width: 466px;
    height: 466px;
    border-radius: 50%;
    box-sizing: border-box;
  }
  .card--back {
    left: 64px;
    background: var(--plum);
    color: var(--paper);
    text-align: center;
  }
  .card--front {
    left: 584px;
    background: var(--paper);
  }
  .contact {
    position: absolute;
    left: 0;
    right: 0;
    top: 92px;
  }
  .contact__name {
    font-family: "Mr Dafoe", cursive;
    font-size: 64px;
    line-height: 1;
    margin: 0;
    font-weight: 400;
  }
  .contact__title {
    font-size: 19px;
    margin: 6px 0 0;
    font-weight: 400;
  }
  .contact__rule {
    width: 72px;
    height: 2px;
    background: var(--paper);
    border: 0;
    margin: 16px auto 16px;
  }
  .contact__address,
  .contact__lines {
    font-size: 19px;
    line-height: 26px;
    margin: 0;
    font-style: normal;
  }
  .contact__lines {
    font-size: 18px;
    line-height: 23px;
    margin-top: 16px;
  }
  .front__ring {
    position: absolute;
    inset: 12px;
    border: 3px solid var(--plum);
    border-radius: 50%;
  }
  .brand {
    position: absolute;
    left: 0;
    right: 0;
    top: 205px;
    text-align: center;
    font-size: 46px;
    font-weight: 400;
    color: var(--teal);
    letter-spacing: 0.5px;
    margin: 0;
  }
</style>
</head>
<body>
<main class="canvas">
  <section class="card card--back">
    <div class="contact">
      <h1 class="contact__name">Daniel Morrow</h1>
      <p class="contact__title">Founder &amp; CEO</p>
      <hr class="contact__rule">
      <address class="contact__address">4312 Juniper Lane<br>Fairbanks, Alaska 99701</address>
      <p class="contact__lines">555-218-4407<br>name@sereneember.com<br>www.sereneember.com</p>
    </div>
  </section>
  <section class="card card--front">
    <div class="front__ring"></div>
    <p class="brand">sereneember.com</p>
  </section>
</main>
</body>
</html>
```